Electrical contracting business specialising in smoke detector installation needs flyer design

i need a flyer design made up highlighting the fact that the Qld legislation is changing on smoke detectors in homes for everyones safety. I am an electrical contractor ( Tallow Bend Electrical) specialising in smoke detector installation to comply with the new Qld legislation. Some of the wording that can be used-
When you sleep, your sense of smell also sleeps. If a fire starts, toxic fumes canovercome you. Photoelectric smoke alarms see smoke and will alert you early, so you can escape. With interconnected alarms, you will be alerted no matter where you are, or where the fire starts.
New legislation specifies the type, positioning and interconnectedness of alarms, which are critical factors for an early warning and a quick escape.
To give your family the best chance of surviving a house fire, update your smoke alarms to match the new legislation as soon as you can. Call Tallow Bend on 0471385269

Target Market(s)

Body Corporates , people selling and renting their properties

Industry/Entity Type

Electrician

Colors

Designer to choose colors to be used in the design.

Requirements
Must have
• Safety aspect.

```html
<!DOCTYPE html>
<html lang="en">
<head>
<meta charset="utf-8">
<title>Sleep Soundly? – Tallow Bend Electrical Flyer</title>
<link href="https://fonts.googleapis.com/css2?family=Lato:wght@700;900&display=swap" rel="stylesheet">
<style>
  :root {
    --page-bg: #e9e6dc;
    --column-dark: #261d24;
    --title-orange: #f0683a;
    --brand-brown: #a5470f;
    --amber-deep: #e0990c;
    --amber-mid: #eeb512;
    --yellow-bright: #f6cf14;
    --ink: #111111;
    --fire-dark: #7a3a12;
    --fire-mid: #d9824a;
    --fire-light: #f0c9a0;
    --ceiling-light: #eef0f2;
    --ceiling-mid: #d8dde2;
  }
  * { box-sizing: border-box; margin: 0; padding: 0; }
  html, body {
    width: 1200px; height: 1200px; overflow: hidden;
    background: var(--page-bg);
    font-family: "Lato", Arial, sans-serif;
  }
  .flyer {
    position: absolute; left: 218px; top: 60px;
    width: 763px; height: 1080px;
    display: flex;
    box-shadow: 0 6px 14px rgba(0,0,0,0.25);
  }
  .brand-column {
    width: 215px; height: 100%;
    background: var(--column-dark);
    position: relative;
  }
  .headline {
    position: absolute; left: 50%; top: 76px;
    transform: translateX(-50%) rotate(180deg);
    writing-mode: vertical-rl;
    font-weight: 700; font-size: 103px; line-height: 1;
    letter-spacing: 1px;
    color: var(--title-orange);
    white-space: nowrap;
  }
  .brand-name {
    position: absolute; left: 0; right: 0; bottom: 50px;
    text-align: center;
    font-weight: 700; font-size: 30px; line-height: 1.1;
    color: var(--brand-brown);
  }
  .content-column {
    width: 548px; height: 100%;
    display: flex; flex-direction: column;
  }
  .copy-block {
    padding: 0 16px 0 26px;
    color: var(--ink);
    font-weight: 700; font-size: 23.5px; line-height: 28.6px;
    white-space: nowrap;
    display: flex; flex-direction: column; justify-content: center;
  }
  .copy-intro {
    height: 249px;
    background: linear-gradient(180deg, var(--amber-deep), var(--amber-mid));
    padding-bottom: 12px;
  }
  .copy-legislation {
    height: 135px;
    background: linear-gradient(180deg, var(--amber-mid), var(--yellow-bright));
  }
  .copy-action {
    height: 177px;
    background: linear-gradient(180deg, var(--amber-mid), var(--amber-deep));
    justify-content: flex-start; padding-top: 10px;
  }
  .call-line {
    font-weight: 900; font-size: 31px; line-height: 1.2; margin-top: 4px;
  }
  .photo { display: block; }
  .photo-smoke-alarm {
    height: 297px;
    background: radial-gradient(ellipse at 45% 40%, var(--fire-light) 0%, var(--fire-mid) 50%, var(--fire-dark) 100%);
  }
  .photo-install-wrap {
    height: 222px;
    background: var(--yellow-bright);
  }
  .photo-install {
    width: 540px; height: 222px;
    background: linear-gradient(135deg, var(--ceiling-light), var(--ceiling-mid));
  }
</style>
</head>
<body>
  <div class="flyer">
    <aside class="brand-column">
      <h1 class="headline">SLEEP SOUNDLY?</h1>
      <div class="brand-name">Tallow<br>Bend</div>
    </aside>
    <main class="content-column">
      <section class="copy-block copy-intro">
        <p>When you sleep, your sense of smell also<br>sleeps. If a fire starts, toxic fumes can<br>overcome you. Photoelectric smoke alarms<br>see smoke and will alert you early, so you can<br>escape. With interconnected alarms, you will<br>be alerted no matter where you are, or where<br>the fire starts.</p>
      </section>
      <div class="photo photo-smoke-alarm" role="img" aria-label="Photo of a white smoke alarm on a timber ceiling with smoke and fire glow rising beneath it"></div>
      <section class="copy-block copy-legislation">
        <p>New legislation specifies the type,<br>positioning and interconnectedness of<br>alarms, which are critical factors for an early<br>warning and a quick escape.</p>
      </section>
      <div class="photo-install-wrap">
        <div class="photo photo-install" role="img" aria-label="Photo of hands wiring a smoke alarm into a white ceiling"></div>
      </div>
      <section class="copy-block copy-action">
        <p>To give your family the best chance of<br>surviving a house fire, update your smoke<br>alarms to match the new legislation as<br>soon as you can.</p>
        <p class="call-line">Call Tallow Bend on 0471385269</p>
      </section>
    </main>
  </div>
</body>
</html>
```